quiet meadow therapy (QMT)

I need to build a website for my therapy business.
There are two parts to the website
on the landing page; they choose whether they are therapists making a referral or patients needing more information.
After that, they are taken to their respective pages.
There is the textual information and a referral form on the therapist page, and on the patient page, the text is a bit different, and there will be a booking page on the patient page.
Visually minimal, it's a therapeutic website. I want it clean, clinical, and modern
colors: greenish blue or maybe orangish
PHP/html code
Updates

Hi everyone
I'm very sorry for the lack of responses to your designs. I am trying to work it out, but this platform has been a challenge for me.
I appreciate everyone's efforts, and I am unsure how to rate designs and move forward with the ones I like. There is a 5-star rating, but I don't understand how I'm supposed to politely say that it is not it without feeling like I'm going to affect someone's future rating negatively.
Please understand me. Thank you

Designs look the same

Target Market(s)

therapy and stress management

Industry/Entity Type

stress management therapy

Coding

Coded - Design and coding required

Number of Pages Required

5+ page

Font styles to use
Serif

Colors
0094D4
00A9DD
6FCCEA
C7EBF8
E9F6FB
00AB8E
00BBA5
67D7C9
C6EFE9
E9F9F6

Requirements
Must have
• landing page that that have 2 options. one for therapist another for patient

```html
<!DOCTYPE html>
<html lang="en">
<head>
<meta charset="utf-8">
<title>Quiet Meadow Therapy</title>
<link href="https://fonts.googleapis.com/css2?family=Figtree:wght@400;500;600;700;800;900&display=swap" rel="stylesheet">
<style>
:root{
  --orange:#F7931E;
  --blue:#0094D4;
  --blue-soft:#E9F6FB;
  --card:#E2F2F9;
  --teal-faint:#D6EEEE;
  --ink:#2E2E2E;
  --text:#6B6B6B;
  --white:#FFFFFF;
  --rule:#8A8A8A;
}
*{margin:0;padding:0;box-sizing:border-box}
html,body{width:1200px;height:3480px;overflow:hidden}
body{position:relative;font-family:"Figtree",sans-serif;color:var(--text);background:var(--white)}
.abs{position:absolute}
.center{left:0;width:1200px;text-align:center}

/* header */
.site-header{top:0;left:0;width:1200px;height:90px;background:var(--white);z-index:5}
.nav-link{top:38px;font-size:12px;font-weight:600;color:var(--ink);letter-spacing:.3px}
.brand{left:520px;top:18px;width:160px;height:56px;display:flex;align-items:center;gap:8px;color:var(--ink)}
.brand-dot{width:30px;height:30px;border-radius:50%;background:#3DBFAE;flex:none}
.brand-text{font-weight:600;line-height:1}
.brand-name{font-size:38px;letter-spacing:12px}
.brand-tag{font-size:7px;letter-spacing:1.2px;margin-top:4px}
.call-btn{left:960px;top:27px;width:179px;height:35px;border-radius:18px;background:var(--orange);color:var(--white);font-size:13px;font-weight:700;display:flex;align-items:center;justify-content:center}

/* hero */
.hero-photo{top:90px;left:0;width:1200px;height:590px;background:linear-gradient(110deg,#3a3632 0%,#6b625a 35%,#8a7f74 55%,#4a4440 80%,#2e2a28 100%)}
.hero-shade{top:90px;left:0;width:1200px;height:590px;background:rgba(20,20,20,.35)}
.page-bg{top:600px;left:0;width:1200px;height:1710px}
.hero-title{top:198px;font-size:56px;font-weight:800;color:var(--white);letter-spacing:-.5px}
.hero-title span{color:var(--orange)}
.hero-sub{top:278px;font-size:22px;color:var(--white)}

.choice-panel{left:390px;top:413px;width:419px;height:261px;background:var(--white);border-radius:4px;box-shadow:0 3px 12px rgba(0,0,0,.12);display:flex}
.choice{width:50%;text-align:center;padding-top:32px}
.choice+.choice{border-left:1px solid #ECECEC}
.choice-icon{width:52px;height:60px;margin:0 auto;border-radius:26px 26px 8px 8px}
.choice-icon.blue{background:#BFE4F4}
.choice-icon.orange{background:#FCDDB8}
.choice-kicker{margin-top:14px;font-size:12px;color:var(--text)}
.choice-title{font-size:22px;font-weight:600;margin-top:2px}
.choice-title.blue{color:var(--blue)}
.choice-title.orange{color:var(--orange)}
.choice-text{font-size:11.5px;line-height:22px;margin:10px auto 0;width:180px}

/* headings */
.section-title{font-size:33px;font-weight:500;color:var(--orange)}
.rule{width:30px;height:2px;background:var(--rule);left:585px}
.btn{height:37px;border-radius:19px;background:var(--orange);color:var(--white);font-size:13px;font-weight:600;display:flex;align-items:center;justify-content:center;letter-spacing:.3px}

.faint-circle{border-radius:50%;background:var(--teal-faint);opacity:.55}

.intro-text{left:230px;width:740px;top:818px;font-size:17px;line-height:30px;text-align:center}

/* services */
.services-panel{left:30px;top:1102px;width:1170px;height:607px;background:var(--white);border-radius:30px 0 0 30px}
.service-card{top:1252px;width:255px;height:315px;background:var(--card);border-radius:3px;text-align:center;padding-top:35px}
.service-icon{width:86px;height:90px;margin:0 auto;border-radius:43px 43px 10px 10px;background:#C4E6F4}
.service-title{margin-top:29px;font-size:16px;font-weight:500;color:var(--ink)}
.service-text{margin:8px auto 0;width:215px;font-size:12px;line-height:21.6px}

/* team */
.portrait{width:187px;height:187px;border-radius:50%}

/* testimonial */
.quote-mark{top:2448px;font-size:40px;font-weight:700;font-style:italic;color:var(--orange);letter-spacing:-4px}
.quote-text{left:300px;width:600px;top:2496px;font-size:17px;line-height:30px;text-align:center}
.quote-name{top:2659px;font-size:12px;font-weight:500;color:var(--ink)}
.dot{top:2704px;width:7px;height:7px;border-radius:50%;background:#CDE9F5}
.dot.active{background:var(--blue)}

/* story */
.story-box{left:59px;top:2790px;width:1080px;height:321px;border:1.5px solid var(--orange)}
.story-text{left:300px;width:600px;top:2928px;font-size:14px;line-height:24px;text-align:center}

/* footer */
.footer-bg{top:3110px;left:0;width:1200px;height:325px;background:linear-gradient(100deg,#ECECEC 0%,#FAFAFA 45%,#F2F2F2 70%,#D9D9D9 100%)}
.footer-brand{left:59px;top:3188px;width:170px;height:56px}
.social{top:3270px;width:32px;height:32px;border-radius:50%;border:1.5px solid var(--orange)}
.social.filled{background:var(--orange)}
.footer-heading{top:3186px;font-size:16px;font-weight:500;color:var(--orange)}
.footer-rule{top:3213px;width:20px;height:1.5px;background:var(--rule)}
.footer-list{list-style:none;font-size:12.5px;color:var(--ink)}
.footer-list li{height:26.2px}
.footer-list li::before{content:"• ";color:var(--text)}
.news-text{left:855px;top:3226px;width:290px;font-size:12.5px;line-height:19px;color:var(--ink)}
.news-input{left:855px;top:3283px;width:284px;height:35px;border:1px solid #D6D6D6;border-radius:18px;background:var(--white);font-size:12.5px;color:var(--ink);padding:10px 0 0 18px}
.news-send{left:1104px;top:3283px;width:35px;height:35px;border-radius:50%;background:var(--orange)}
.copyright{top:3435px;left:0;width:1200px;height:45px;background:var(--orange);color:var(--white);font-size:11px;display:flex;align-items:center;justify-content:center}
</style>
</head>
<body>

<!-- hero background -->
<div class="abs hero-photo" role="img" aria-label="Photo of a family and therapist giving a high five"></div>
<div class="abs hero-shade"></div>
<svg class="abs" style="top:600px;left:0" width="1200" height="1710" viewBox="0 0 1200 1710">
  <path d="M0,15 Q560,115 1200,62 L1200,1710 L0,1710 Z" fill="#E9F6FB"/>
</svg>

<header class="abs site-header">
  <span class="abs nav-link" style="left:61px">ABOUT</span>
  <span class="abs nav-link" style="left:146px">SERVICES</span>
  <span class="abs nav-link" style="left:246px">THERAPISTS</span>
  <span class="abs nav-link" style="left:359px">PATIENTS</span>
  <div class="abs brand">
    <div class="brand-dot"></div>
    <div class="brand-text">
      <div class="brand-name">QMT</div>
      <div class="brand-tag">QUIET MEADOW THERAPY</div>
    </div>
  </div>
  <span class="abs nav-link" style="left:785px">BLOG</span>
  <span class="abs nav-link" style="left:861px">CONTACT</span>
  <div class="abs call-btn">CALL: (555) 014-2290</div>
</header>

<h1 class="abs center hero-title"><span>LIVE THE LIFE</span> YOU WANT</h1>
<p class="abs center hero-sub">Lorem ipsum dolor sit amet, consectetuer adipiscing elit.</p>

<div class="abs choice-panel">
  <div class="choice">
    <div class="choice-icon blue" role="img" aria-label="Therapist icon"></div>
    <div class="choice-kicker">I'm A</div>
    <div class="choice-title blue">THERAPISTS</div>
    <p class="choice-text">Lorem ipsum dolor sit amet, consectetuer adipiscing elit, sed diam nonummy nibh.</p>
  </div>
  <div class="choice">
    <div class="choice-icon orange" role="img" aria-label="Patient icon"></div>
    <div class="choice-kicker">I'm A</div>
    <div class="choice-title orange">PATIENTS</div>
    <p class="choice-text">Lorem ipsum dolor sit amet, consectetuer adipiscing elit, sed diam nonummy nibh.</p>
  </div>
</div>

<!-- intro -->
<div class="abs faint-circle" style="left:334px;top:716px;width:532px;height:532px"></div>
<h2 class="abs center section-title" style="top:742px">Overcome Yourself To Love Yourself.</h2>
<div class="abs rule" style="top:793px"></div>
<p class="abs intro-text">Lorem ipsum dolor sit amet, consectetuer adipiscing elit, sed diam nonummy nibh euismod tincidunt ut laoreet dolore magna aliquam erat volutpat. Ut wisi enim ad minim veniam, quis nostrud exerci tation ullamcorper suscipit lobortis nisl ut aliquip ex ea commodo consequat. Duis autem vel eum iriure dolor in hendrerit in vulputate velit esse molestie consequat, vel illum dolore eu feugiat nulla facilisis.</p>
<div class="abs btn" style="left:540px;top:990px;width:119px">READ MORE</div>

<!-- services -->
<div class="abs faint-circle" style="left:328px;top:1572px;width:544px;height:544px"></div>
<section class="abs services-panel"></section>
<h2 class="abs center section-title" style="top:1169px">We're Here To Help You Change Your Life.</h2>
<div class="abs rule" style="top:1220px"></div>

<div class="abs service-card" style="left:59px">
  <div class="service-icon" role="img" aria-label="Stress management icon"></div>
  <div class="service-title">Stress Management Therapy</div>
  <p class="service-text">Lorem ipsum dolor sit amet, consectetuer adipiscing elit, sed diam nonummy nibh euismod tincidunt ut laoreet dolore magna aliquam erat volutpat.</p>
</div>
<div class="abs service-card" style="left:335px">
  <div class="service-icon" role="img" aria-label="Individual counseling icon"></div>
  <div class="service-title">Individual Counseling</div>
  <p class="service-text">Lorem ipsum dolor sit amet, consectetuer adipiscing elit, sed diam nonummy nibh euismod tincidunt ut laoreet dolore magna aliquam erat volutpat.</p>
</div>
<div class="abs service-card" style="left:611px">
  <div class="service-icon" role="img" aria-label="Couple counseling icon"></div>
  <div class="service-title">Couple Counseling</div>
  <p class="service-text">Lorem ipsum dolor sit amet, consectetuer adipiscing elit, sed diam nonummy nibh euismod tincidunt ut laoreet dolore magna aliquam erat volutpat.</p>
</div>
<div class="abs service-card" style="left:885px">
  <div class="service-icon" role="img" aria-label="Family counseling icon"></div>
  <div class="service-title">Family Counseling</div>
  <p class="service-text">Lorem ipsum dolor sit amet, consectetuer adipiscing elit, sed diam nonummy nibh euismod tincidunt ut laoreet dolore magna aliquam erat volutpat.</p>
</div>
<div class="abs btn" style="left:517px;top:1598px;width:165px">CONTACT US NOW</div>

<!-- specialists -->
<h2 class="abs center section-title" style="top:1777px">Get Help From A Specialist</h2>
<div class="abs rule" style="top:1827px"></div>
<div class="abs portrait" style="left:60px;top:1860px;background:linear-gradient(135deg,#6a4a32,#c99a70)" role="img" aria-label="Specialist portrait"></div>
<div class="abs portrait" style="left:284px;top:1860px;background:linear-gradient(135deg,#9a9690,#d8c7b8)" role="img" aria-label="Specialist portrait"></div>
<div class="abs portrait" style="left:507px;top:1860px;background:linear-gradient(135deg,#4c6a85,#9a7a66)" role="img" aria-label="Specialist portrait"></div>
<div class="abs portrait" style="left:730px;top:1860px;background:linear-gradient(135deg,#b8b4a8,#8a6a58)" role="img" aria-label="Specialist portrait"></div>
<div class="abs portrait" style="left:953px;top:1860px;background:linear-gradient(135deg,#7c8a8c,#b08a74)" role="img" aria-label="Specialist portrait"></div>
<div class="abs portrait" style="left:172px;top:2048px;background:linear-gradient(135deg,#f2f2f2,#b58a70)" role="img" aria-label="Specialist portrait"></div>
<div class="abs portrait" style="left:395px;top:2048px;background:linear-gradient(135deg,#5a5a3a,#d8b890)" role="img" aria-label="Specialist portrait"></div>
<div class="abs portrait" style="left:618px;top:2048px;background:linear-gradient(135deg,#6c7a80,#c49a7c)" role="img" aria-label="Specialist portrait"></div>
<div class="abs portrait" style="left:841px;top:2048px;background:linear-gradient(135deg,#ffffff,#8a6a50)" role="img" aria-label="Specialist portrait"></div>

<!-- testimonial -->
<h2 class="abs center section-title" style="top:2377px">What Our Patients Are Saying</h2>
<div class="abs rule" style="top:2427px"></div>
<div class="abs center quote-mark">//</div>
<p class="abs quote-text">Lorem ipsum dolor sit amet, consectetuer adipiscing elit, sed diam nonummy nibh euismod tincidunt ut laoreet dolore magna aliquam erat volutpat. Ut wisi enim ad minim veniam, quis nostrud exerci tation ullamcorper suscipit lobortis nisl ut aliquip ex ea commodo consequat. Duis autem vel eum iriure dolor in hendrerit in vulputate velit esse molestie consequat.</p>
<div class="abs center quote-name">Nora Vale</div>
<div class="abs dot active" style="left:562px"></div>
<div class="abs dot" style="left:585px"></div>
<div class="abs dot" style="left:607px"></div>
<div class="abs dot" style="left:630px"></div>

<!-- footer background -->
<div class="abs footer-bg" role="img" aria-label="Misty lake landscape with a paddleboarder"></div>

<!-- story -->
<div class="abs story-box"></div>
<div class="abs faint-circle" style="left:76px;top:2791px;width:202px;height:202px;opacity:.4"></div>
<div class="abs faint-circle" style="left:920px;top:2966px;width:202px;height:202px;opacity:.4"></div>
<h2 class="abs center section-title" style="top:2858px">Do You Have A Story To Tell?</h2>
<div class="abs rule" style="top:2906px"></div>
<p class="abs story-text">Lorem ipsum dolor sit amet, consectetuer adipiscing elit, sed diam nonummy nibh euismod tincidunt ut laoreet dolore magna aliquam erat volutpat.</p>
<div class="abs btn" style="left:517px;top:3000px;width:165px">CONTACT US NOW</div>

<!-- footer -->
<footer>
  <div class="abs brand footer-brand">
    <div class="brand-dot"></div>
    <div class="brand-text">
      <div class="brand-name">QMT</div>
      <div class="brand-tag">QUIET MEADOW THERAPY</div>
    </div>
  </div>
  <div class="abs social filled" style="left:64px" aria-label="Social link"></div>
  <div class="abs social" style="left:104px" aria-label="Social link"></div>
  <div class="abs social" style="left:145px" aria-label="Social link"></div>
  <div class="abs social" style="left:185px" aria-label="Social link"></div>

  <div class="abs footer-heading" style="left:346px">Quick Links</div>
  <div class="abs footer-rule" style="left:346px"></div>
  <ul class="abs footer-list" style="left:344px;top:3228px">
    <li>About</li><li>Services</li><li>Therapists</li><li>Patients</li><li>Blog</li><li>Contact</li>
  </ul>

  <div class="abs footer-heading" style="left:557px">Our Services</div>
  <div class="abs footer-rule" style="left:557px"></div>
  <ul class="abs footer-list" style="left:555px;top:3228px">
    <li>Stress management therapy</li><li>Individual Counseling</li><li>Couple Counseling</li><li>Family Counseling</li>
  </ul>

  <div class="abs footer-heading" style="left:855px">Newsletter</div>
  <div class="abs footer-rule" style="left:855px"></div>
  <p class="abs news-text">Stay Connected! Get Latest News &amp; Updates Straight To Your inbox.</p>
  <div class="abs news-input">Email</div>
  <svg class="abs news-send" viewBox="0 0 35 35" width="35" height="35">
    <circle cx="17.5" cy="17.5" r="17.5" fill="#F7931E"/>
    <path d="M10 18 L25 11 L20 26 L17 19 Z" fill="#FFFFFF"/>
  </svg>

  <div class="abs copyright">© QUIET MEADOW THERAPY - 2022. All Rights Reserved.</div>
</footer>

</body>
</html>
```